BrightLaneHouses.Com needs a email flyer to be sent to Realtors about our awesome mortgage services!

We are a real estate and mortgage company. This flyer will advertise the USPs of our mortgage services to Realtors. The intent is for these Realtors to contact us and then have their buyer clients contact us for a real estate mortgage loan.
The flyer will be email blasted to Realtors.
Size is 8.5 x 11 inches i.e. US Letter size. (Portrait in Orientation)
***This is an eFlyer and will be delivered by email, it is not a print flyer.
IN THE ATTACHMENT you'll find the text needed in the flyer.
For theme colors and added details you may go to our website:
www.brightlanehouses.com
Industry/Entity Type
Real Estate
Look and feel
Each slider illustrates characteristics of the customer's brand and the style your logo design should communicate.

```html
<!DOCTYPE html>
<html lang="en">
<head>
<meta charset="utf-8">
<title>BrightLaneHouses.Com – Realtor Mortgage Flyer</title>
<link href="https://fonts.googleapis.com/css2?family=Quicksand:wght@400&display=swap" rel="stylesheet">
<style>
  :root {
    --page: #ffffff;
    --slate: #4a4866;
    --silver-dark: #9a9a9e;
    --silver-light: #ffffff;
    --leaf: #86bd3c;
    --pale-leaf: #c9d8b0;
    --rim: #b9b9bf;
    --accent-red: #e0174f;
    --lime-text: #8fd130;
    --ink: #141414;
    --link-blue: #1f3fe0;
    --bullet-green: #3e5a1c;
  }
  html, body {
    margin: 0;
    width: 1200px;
    height: 1200px;
    overflow: hidden;
    background: var(--page);
  }
  .flyer {
    position: absolute;
    left: 128px;
    top: 0;
    width: 882px;
    height: 1200px;
    overflow: hidden;
    font-family: "Quicksand", sans-serif;
    font-size: 24px;
    letter-spacing: 2.1px;
    line-height: 33px;
    white-space: nowrap;
  }
  .backdrop { position: absolute; inset: 0; width: 882px; height: 1200px; }
  .line { position: absolute; margin: 0; }
  .theme { color: var(--accent-red); }
  .pitch { color: var(--lime-text); }
  .point { color: var(--ink); }
  .point.red { color: var(--accent-red); }
  .point.blue { color: var(--link-blue); }
  .dot {
    position: absolute;
    left: -6px;
    width: 11px;
    height: 13px;
    border-radius: 50%;
    background: var(--bullet-green);
  }
  .dot.red { background: var(--accent-red); }
  .dot.blue { background: var(--link-blue); }
  .star {
    position: absolute;
    width: 18px;
    height: 18px;
    fill: var(--ink);
  }
  .blank {
    position: absolute;
    background: var(--page);
  }
</style>
</head>
<body>
<main class="flyer">
  <svg class="backdrop" viewBox="0 0 1102 1500" preserveAspectRatio="none" aria-hidden="true">
    <defs>
      <linearGradient id="silver" x1="0" y1="0" x2="1" y2="0">
        <stop offset="0" stop-color="var(--silver-dark)"/>
        <stop offset="0.5" stop-color="var(--silver-light)"/>
        <stop offset="1" stop-color="var(--silver-dark)"/>
      </linearGradient>
      <linearGradient id="silverSoft" x1="0" y1="0" x2="0" y2="1">
        <stop offset="0" stop-color="#d6d6da"/>
        <stop offset="1" stop-color="#ffffff"/>
      </linearGradient>
    </defs>
    <rect width="1102" height="1500" fill="var(--slate)"/>
    <path d="M0 0 H1102 V75 Q560 310 0 135 Z" fill="url(#silver)"/>
    <path d="M0 0 H1102 V60 Q560 255 0 90 Z" fill="url(#silverSoft)"/>
    <path d="M0 612 C520 600 1010 1000 1102 1500 L0 1500 Z" fill="var(--rim)"/>
    <path d="M0 634 C490 625 980 1010 1075 1500 L0 1500 Z" fill="var(--leaf)"/>
    <path d="M0 742 C390 740 880 1060 970 1500 L0 1500 Z" fill="var(--pale-leaf)"/>
  </svg>

  <div class="blank" style="left:814px; top:4px; width:60px; height:312px;"></div>
  <div class="blank" style="left:796px; top:661px; width:70px; height:94px;"></div>
  <div class="blank" style="left:0; top:1072px; width:78px; height:124px;"></div>

  <p class="line theme" style="left:64px; top:46px;">Theme:Get more referrals from your buyer clients:</p>
  <p class="line theme" style="left:54px; top:79px;">be a super hero buyers' agent.</p>

  <p class="line pitch" style="left:6px; top:181px;">Get your buyers their dream homes &nbsp;AND a dream interest<br>rate..</p>
  <p class="line pitch" style="left:8px; top:240px;">We are meeting deadlines, closing and funding on time,<br>&nbsp;originating loans loans since 2001.</p>
  <p class="line pitch" style="left:6px; top:309px;">Today's rate 3.75%.</p>
  <p class="line pitch" style="left:6px; top:345px;">Tody's closing cost credit.</p>
  <p class="line pitch" style="left:8px; top:383px;">Halloway's of service and Thriftmoors of rates.</p>
  <p class="line pitch" style="left:10px; top:419px;">Maximize your referrals from your clients when you refer them<br>to a lender who:</p>

  <span class="dot" style="top:505px;"></span>
  <p class="line point" style="left:18px; top:494px;">Will encourage them to shop.</p>
  <span class="dot" style="top:545px;"></span>
  <p class="line point" style="left:22px; top:534px;">Offer them mortgage rates comparable to interest lenders.</p>
  <span class="dot" style="top:587px;"></span>
  <p class="line point" style="left:22px; top:576px;">Offer super low OR NO closing Cost comparable to internet<br>lenders</p>
  <span class="dot" style="top:658px;"></span>
  <p class="line point" style="left:24px; top:653px;">Is your local lender and your clients can meet in person.</p>
  <span class="dot red" style="top:701px;"></span>
  <p class="line point red" style="left:24px; top:690px;">In house processing of all loan files.</p>
  <span class="dot blue" style="top:737px;"></span>
  <p class="line point blue" style="left:24px; top:726px;">www.brightlaneloans.com</p>
  <span class="dot" style="top:774px;"></span>
  <p class="line point" style="left:20px; top:763px;">Be the hero when you find them their dream home and also get<br>them an interest rate that make their friends &amp; neighbour jealous.</p>
  <span class="dot" style="top:838px;"></span>
  <p class="line point blue" style="left:20px; top:833px;">Remember we are Halloway's of service and Thriftmoor of rates.</p>

  <svg class="star" style="left:35px; top:876px;" viewBox="0 0 24 24" aria-hidden="true"><path d="M12 1l3.1 7.3 7.9.7-6 5.2 1.8 7.8L12 17.9 5.2 22l1.8-7.8-6-5.2 7.9-.7z"/></svg>
  <p class="line point" style="left:73px; top:871px;">2285 Larkspur Ave 210 Denver CO 80231</p>
  <svg class="star" style="left:35px; top:912px;" viewBox="0 0 24 24" aria-hidden="true"><path d="M12 1l3.1 7.3 7.9.7-6 5.2 1.8 7.8L12 17.9 5.2 22l1.8-7.8-6-5.2 7.9-.7z"/></svg>
  <p class="line point" style="left:73px; top:907px;">Call Daniel Keswick 303-555-0148.</p>
  <svg class="star" style="left:35px; top:948px;" viewBox="0 0 24 24" aria-hidden="true"><path d="M12 1l3.1 7.3 7.9.7-6 5.2 1.8 7.8L12 17.9 5.2 22l1.8-7.8-6-5.2 7.9-.7z"/></svg>
  <p class="line point" style="left:77px; top:946px;">Daniel@BrightLaneHouses.Com.</p>
  <svg class="star" style="left:35px; top:996px;" viewBox="0 0 24 24" aria-hidden="true"><path d="M12 1l3.1 7.3 7.9.7-6 5.2 1.8 7.8L12 17.9 5.2 22l1.8-7.8-6-5.2 7.9-.7z"/></svg>
  <p class="line point" style="left:88px; top:993px;">Not for consumer use, for mortgage and Real Estate<br>Professionals ONLY. This does not meet TILA or RESPA<br>requirements for advertising.</p>
  <svg class="star" style="left:90px; top:1097px;" viewBox="0 0 24 24" aria-hidden="true"><path d="M12 1l3.1 7.3 7.9.7-6 5.2 1.8 7.8L12 17.9 5.2 22l1.8-7.8-6-5.2 7.9-.7z"/></svg>
  <p class="line point" style="left:122px; top:1087px;">Licenses: NMLS# 481206,593714, Colorado LMB 100027741<br>EA 40028815.</p>
  <svg class="star" style="left:90px; top:1155px;" viewBox="0 0 24 24" aria-hidden="true"><path d="M12 1l3.1 7.3 7.9.7-6 5.2 1.8 7.8L12 17.9 5.2 22l1.8-7.8-6-5.2 7.9-.7z"/></svg>
  <p class="line point" style="left:124px; top:1150px;">Regulated by the division of Real Estate.</p>
</main>
</body>
</html>
```